Premium Corporate Website Design for Velmora Systems

Our company Velmora Systems GmbH (formerly BrightHarbor GmbH) is looking for a new, modern, and professional corporate website. The content should be based on our existing site bright-harbor.example
, but reimagined in a contemporary, tech-oriented, and premium design.

Requirements:

- Alignment with the new Velmora Systems logo and corporate identity
- Modern layout that reflects the tech and IT consulting industry
- Clear and user-friendly structure with intuitive navigation
- Premium look and feel that highlights our market position
- Incorporation of animated or interactive elements to add dynamism
- Design should clearly stand out from competitors such as Durlak GmbH, TMPulse, Vorndal, Marvix, and Holtreuven
- International focus: Since our company also operates in the U.S. market, the website should reflect a global presence (e.g., bilingual structure in German/English, international visual language, U.S.-inspired corporate design elements)

Goal:
To create a high-quality, innovative, and brand-strong website that positions Velmora Systems GmbH as a modern, trustworthy, and future-oriented IT consulting company — both in the German-speaking region and in the United States.

In addition to the design, we would also like the website to be delivered as functional HTML/CSS files (or WordPress implementation if possible).

All images from our current website www.bright-harbor.example
can be used if needed. Designers are welcome to reuse or adapt this material where appropriate."

Target Market(s)

Medium to large enterprises in the technology, finance, and energy sectors Companies seeking premium IT consulting, quality assurance, and test automation services Decision makers and executives (CIOs, CTOs, IT managers) in Europe and the United States A global audience that values innovation, professionalism, and trust

Industry/Entity Type

Information Technology & Consulting Software Testing & Quality Assurance Technology / Professional Services

Coding

Number of Pages Required

Requirements
Must have
• - Integration of the Velmora Systems logo and corporate identity - Bilingual setup (German & English) Modern, premium tech design with a professional look and feel Clear structure and intuitive navigation for easy usability Responsive design, optimized for desktop, tablet, and mobile High-quality visuals and dynamic elements (animations, interactive features) Strong differentiation from competitors (Durlak GmbH, TMPulse, Vorndal, Marvix, Holtreuven)
Nice to have
• Subtle micro-animations and hover effects to enhance user experience Custom icons or illustrations that align with the Velmora brand Dark/Light mode toggle for modern usability Blog or insights section to share expertise and updates SEO-friendly structure for better visibility in search engines Integration of social media feeds (LinkedIn, Facebook, Instagram) Contact form with automation (e.g., PHPMailer or CRM integration) Showcasing case studies or success stories with an engaging layout
Should not have
• Overly crowded or cluttered layouts Stock images that look generic or low quality Outdated design styles (e.g., gradients from the 2000s, heavy drop shadows) Complex navigation that confuses users Excessive use of bright or non-brand colors outside the Velmora identity Long loading times caused by oversized media files Pop-ups or intrusive ads that disrupt the premium brand image

```html
<!DOCTYPE html>
<html lang="en">
<head>
<meta charset="utf-8">
<title>Velmora Systems — Software. Testing. Consulting.</title>
<link rel="stylesheet" href="https://fonts.googleapis.com/css2?family=Space+Grotesk:wght@500;600;700&family=Inter:wght@400;500;600;700&display=swap">
<style>
:root{
  --canvas:#ffffff;
  --bg:#05080c;
  --surface:#0a0f15;
  --surface-2:#0e141b;
  --border:#161e27;
  --accent:#0fb2d8;
  --accent-soft:rgba(15,178,216,.12);
  --text:#f4f7fa;
  --muted:#8a939d;
  --dim:#5d6670;
}
*{box-sizing:border-box;margin:0;padding:0}
html,body{width:1200px;height:1200px;overflow:hidden;background:var(--canvas)}
body{position:relative;font-family:'Inter',sans-serif;color:var(--text)}
.site{position:absolute;left:442px;top:0;width:1280px;height:4868px;background:var(--bg);transform:scale(.2465);transform-origin:0 0;overflow:hidden}
.container{width:1080px;margin:0 auto;position:relative}
h1,h2,h3,.brand{font-family:'Space Grotesk',sans-serif}
.accent{color:var(--accent)}
svg.ic{width:22px;height:22px;fill:none;stroke:var(--accent);stroke-width:1.8;stroke-linecap:round;stroke-linejoin:round}

/* nav */
.nav{height:56px;border-bottom:1px solid var(--border)}
.nav .container{display:flex;align-items:center;height:56px}
.brand{color:var(--accent);font-weight:700;font-size:21px}
.nav-links{display:flex;gap:30px;margin-left:auto;margin-right:auto;padding-left:150px;font-size:14px;font-weight:500}
.btn{display:inline-flex;align-items:center;justify-content:center;gap:8px;border-radius:6px;font-weight:600;font-size:14px}
.btn-primary{background:var(--accent);color:#fff}
.nav .btn{height:32px;padding:0 16px;font-size:12px}

/* hero */
.hero{height:680px;text-align:center;padding-top:92px;position:relative}
.hero-bg{position:absolute;inset:0;background:radial-gradient(ellipse at 50% 45%,rgba(40,70,110,.22),transparent 60%),linear-gradient(180deg,#070b11 0%,#0a0f1a 70%,#0c1220 100%)}
.hero > *:not(.hero-bg){position:relative}
.hero h1{font-size:64px;line-height:70px;font-weight:700;letter-spacing:-.5px}
.hero p{width:650px;margin:18px auto 0;font-size:18px;line-height:28px;color:#aab2bb}
.hero-actions{margin-top:26px;display:flex;justify-content:center;gap:26px;align-items:center}
.hero-actions .btn-primary{height:36px;padding:0 22px}
.hero-actions .link{font-size:15px;font-weight:600}
.pillars{display:flex;justify-content:center;gap:26px;margin-top:48px}
.pillar{width:246px;height:174px;border:1px solid var(--border);border-radius:10px;background:rgba(10,15,21,.6);padding-top:26px}
.pillar svg.ic{width:38px;height:38px;stroke-width:1.6}
.pillar h3{font-family:'Inter',sans-serif;font-size:15px;font-weight:600;margin-top:10px}
.pillar p{width:180px;margin:10px auto 0;font-size:13px;line-height:21px;color:var(--muted)}

/* section heads */
.head{text-align:center}
.head h2{font-size:44px;line-height:48px;font-weight:700}
.head p{margin:14px auto 0;font-size:16px;line-height:25px;color:var(--muted)}

/* services */
.services{height:1134px;padding-top:84px}
.services .head p{width:680px}
.grid-3{display:grid;grid-template-columns:repeat(3,338px);gap:32px 33px;margin-top:62px}
.card{background:var(--surface);border:1px solid var(--border);border-radius:10px}
.service{height:366px;padding:20px 22px}
.icon-box{width:44px;height:44px;border-radius:8px;background:var(--accent-soft);display:flex;align-items:center;justify-content:center}
.service h3{font-size:18px;font-weight:600;margin-top:24px}
.service .desc{margin-top:14px;font-size:12px;line-height:18px;color:var(--muted)}
.service ul{list-style:none;margin-top:20px}
.service li{font-size:12px;color:#a7afb8;height:25px;display:flex;align-items:center;gap:12px}
.service li::before{content:"";width:5px;height:5px;border-radius:50%;background:var(--accent)}
.service .more{margin-top:16px;height:32px;border-radius:6px;background:var(--surface-2);display:flex;align-items:center;justify-content:center;font-size:12px;font-weight:600}

/* expertise */
.expertise{height:1230px;padding-top:66px}
.pill{display:inline-flex;align-items:center;gap:8px;height:24px;padding:0 14px;border-radius:12px;background:var(--accent-soft);color:var(--accent);font-size:11px;font-weight:500}
.pill::before{content:"";width:5px;height:5px;border-radius:50%;background:var(--accent)}
.expertise .head h2{font-size:56px;line-height:62px;margin-top:24px}
.expertise .head p{width:570px;font-size:18px;line-height:29px;margin-top:12px}
.exp-grid{display:grid;grid-template-columns:repeat(3,338px);gap:43px 33px;margin-top:80px}
.exp{padding:26px 24px;height:295px}
.exp.short{height:285px}
.exp-top{display:flex;gap:20px}
.exp-top .icon-box{flex:none;width:46px;height:46px}
.exp h3{font-size:18px;line-height:24px;font-weight:600}
.exp .desc{margin-top:12px;font-size:12px;line-height:20px;color:var(--muted)}
.tags{display:flex;flex-wrap:wrap;gap:8px 6px;margin-top:18px}
.tags span{font-size:10px;font-weight:600;padding:4px 8px;background:var(--surface-2);border-radius:4px}
.cta{width:450px;height:76px;margin:75px auto 0;display:flex;align-items:center;gap:18px;padding:0 24px}
.cta h4{font-size:15px;font-weight:600}
.cta p{font-size:11px;color:var(--muted);margin-top:6px}

/* about */
.about{height:620px;padding-top:88px}
.about .container{display:flex;justify-content:space-between}
.about-copy{width:500px;padding-top:38px}
.about-copy h2{font-size:44px;line-height:43px;font-weight:700}
.about-copy p{font-size:15px;line-height:25px;color:var(--muted);margin-top:22px}
.about-copy h2 + p{margin-top:30px}
.stats{width:510px;display:grid;grid-template-columns:repeat(2,245px);gap:20px}
.stat{height:205px;text-align:center;padding-top:24px}
.stat .icon-box{margin:0 auto}
.stat strong{display:block;font-family:'Space Grotesk',sans-serif;font-size:27px;color:var(--accent);margin-top:12px}
.stat h4{font-size:15px;font-weight:600;margin-top:8px}
.stat p{width:190px;margin:10px auto 0;font-size:11px;line-height:17px;color:var(--muted)}

/* contact */
.contact{height:846px;padding-top:80px;border-bottom:1px solid var(--border)}
.contact .head p{width:680px;line-height:28px}
.contact-grid{display:flex;justify-content:space-between;margin-top:50px}
.reach{width:520px;padding-top:6px}
.reach h3{font-family:'Inter',sans-serif;font-size:18px;font-weight:600}
.reach-item{display:flex;gap:18px;align-items:center;height:44px;margin-top:20px}
.reach-item .icon-box{width:40px;height:40px}
.reach-item b{display:block;font-size:13px;font-weight:600}
.reach-item span{font-size:13px;color:var(--muted)}
.why{margin-top:36px;height:194px;padding:22px}
.why h4{font-size:15px;font-weight:600}
.why ul{list-style:none;margin-top:16px}
.why li{font-size:13px;color:#a7afb8;height:32px;display:flex;align-items:center;gap:12px}
.why li::before{content:"";width:6px;height:6px;border-radius:50%;background:var(--accent)}
.form{width:517px;height:488px;padding:22px}
.form h4{font-size:14px;font-weight:600}
.row{display:flex;gap:24px}
.field{flex:1;margin-top:22px}
.field label{display:block;font-size:11px;font-weight:600}
.field .input{height:30px;margin-top:10px;border-radius:5px;background:var(--surface-2);border:1px solid var(--border);font-size:10px;color:var(--dim);padding:9px 12px}
.field .input.area{height:106px}
.form .btn{width:100%;height:32px;margin-top:22px;font-size:12px}

/* footer */
.footer{height:302px;padding-top:48px}
.foot-top{display:flex;height:186px}
.foot-brand{width:454px}
.foot-brand p{margin-top:18px;font-size:13px;line-height:21px;color:var(--muted)}
.foot-col{width:278px;margin-left:100px}
.foot-col + .foot-col{margin-left:0}
.foot-col h5{font-size:13px;font-weight:600}
.foot-col a{display:block;font-size:13px;color:var(--muted);margin-top:12px;text-decoration:none}
.foot-bottom{border-top:1px solid var(--border);padding-top:28px;display:flex;justify-content:space-between;font-size:11px;color:var(--muted)}
</style>
</head>
<body>
<svg width="0" height="0" style="position:absolute">
  <defs>
    <symbol id="i-code" viewBox="0 0 24 24"><path d="M8 6l-6 6 6 6M16 6l6 6-6 6"/></symbol>
    <symbol id="i-shield" viewBox="0 0 24 24"><path d="M12 2l8 3v6c0 5-3.5 9-8 11-4.5-2-8-6-8-11V5z"/></symbol>
    <symbol id="i-bolt" viewBox="0 0 24 24"><path d="M13 2L4 14h7l-1 8 9-12h-7z"/></symbol>
    <symbol id="i-tube" viewBox="0 0 24 24"><path d="M10 2h4M11 2v17a1 1 0 002 0V2M11 12h2"/></symbol>
    <symbol id="i-gear" viewBox="0 0 24 24"><circle cx="12" cy="12" r="3"/><path d="M12 2v3M12 19v3M2 12h3M19 12h3M4.9 4.9l2.1 2.1M17 17l2.1 2.1M4.9 19.1L7 17M17 7l2.1-2.1"/></symbol>
    <symbol id="i-users" viewBox="0 0 24 24"><circle cx="9" cy="8" r="4"/><path d="M2 21c0-4 3-6 7-6s7 2 7 6M16 4a4 4 0 010 8M18 15c2.5.5 4 2.5 4 6"/></symbol>
    <symbol id="i-db" viewBox="0 0 24 24"><ellipse cx="12" cy="5" rx="8" ry="3"/><path d="M4 5v14c0 1.7 3.6 3 8 3s8-1.3 8-3V5M4 12c0 1.7 3.6 3 8 3s8-1.3 8-3"/></symbol>
    <symbol id="i-cloud" viewBox="0 0 24 24"><path d="M7 19h10a5 5 0 000-10 7 7 0 00-13 3 4 4 0 003 7z"/></symbol>
    <symbol id="i-lock" viewBox="0 0 24 24"><rect x="4" y="11" width="16" height="10" rx="2"/><path d="M8 11V7a4 4 0 018 0v4"/></symbol>
    <symbol id="i-search" viewBox="0 0 24 24"><circle cx="11" cy="11" r="7"/><path d="M21 21l-5-5"/></symbol>
    <symbol id="i-building" viewBox="0 0 24 24"><rect x="5" y="3" width="14" height="18" rx="1"/><path d="M9 7h2M13 7h2M9 11h2M13 11h2M9 15h2M13 15h2M10 21v-3h4v3"/></symbol>
    <symbol id="i-spark" viewBox="0 0 24 24"><path d="M12 3l2 7 7 2-7 2-2 7-2-7-7-2 7-2z"/></symbol>
    <symbol id="i-globe" viewBox="0 0 24 24"><circle cx="12" cy="12" r="9"/><path d="M3 12h18M12 3c3 3 3 15 0 18M12 3c-3 3-3 15 0 18"/></symbol>
    <symbol id="i-award" viewBox="0 0 24 24"><circle cx="12" cy="9" r="6"/><path d="M9 14l-1 8 4-2 4 2-1-8"/></symbol>
    <symbol id="i-trend" viewBox="0 0 24 24"><path d="M3 17l6-6 4 4 8-8M15 7h6v6"/></symbol>
    <symbol id="i-mail" viewBox="0 0 24 24"><rect x="3" y="5" width="18" height="14" rx="2"/><path d="M3 7l9 6 9-6"/></symbol>
    <symbol id="i-phone" viewBox="0 0 24 24"><path d="M5 3h4l2 5-2.5 1.5a11 11 0 006 6L16 13l5 2v4a2 2 0 01-2 2A17 17 0 013 5a2 2 0 012-2z"/></symbol>
    <symbol id="i-pin" viewBox="0 0 24 24"><path d="M12 22s7-7 7-12a7 7 0 00-14 0c0 5 7 12 7 12z"/><circle cx="12" cy="10" r="2.5"/></symbol>
    <symbol id="i-send" viewBox="0 0 24 24"><path d="M22 2L11 13M22 2l-7 20-4-9-9-4z"/></symbol>
    <symbol id="i-arrow" viewBox="0 0 24 24"><path d="M5 12h14M13 6l6 6-6 6"/></symbol>
  </defs>
</svg>

<div class="site">
  <header class="nav">
    <div class="container">
      <div class="brand">Velmora Systems</div>
      <nav class="nav-links"><span>Services</span><span>Expertise</span><span>About</span><span>Contact</span></nav>
      <span class="btn btn-primary">Get Started</span>
    </div>
  </header>

  <section class="hero">
    <div class="hero-bg" role="img" aria-label="Faint dark circuit-board texture behind the hero"></div>
    <h1><span class="accent">Software.</span> Testing. <span class="accent">Consulting.</span></h1>
    <p>Premium IT consulting services for enterprise transformation. We deliver innovative solutions in software testing, quality assurance, and digital excellence.</p>
    <div class="hero-actions">
      <span class="btn btn-primary">Explore Services <svg class="ic" style="width:14px;height:14px;stroke:#fff"><use href="#i-arrow"/></svg></span>
      <span class="link">View Case Studies</span>
    </div>
    <div class="pillars">
      <div class="pillar"><svg class="ic"><use href="#i-code"/></svg><h3>Innovation</h3><p>Cutting-edge solutions for modern challenges</p></div>
      <div class="pillar"><svg class="ic"><use href="#i-shield"/></svg><h3>Quality</h3><p>Uncompromising standards in every project</p></div>
      <div class="pillar"><svg class="ic"><use href="#i-bolt"/></svg><h3>Excellence</h3><p>Delivering results that exceed expectations</p></div>
    </div>
  </section>

  <section class="services">
    <div class="container">
      <div class="head">
        <h2>Our <span class="accent">Services</span></h2>
        <p>Comprehensive IT solutions designed to accelerate your business transformation and deliver measurable results.</p>
      </div>
      <div class="grid-3">
        <article class="card service">
          <div class="icon-box"><svg class="ic"><use href="#i-tube"/></svg></div>
          <h3>Software Testing &amp; QA</h3>
          <p class="desc">Comprehensive testing strategies including automated testing, performance testing, and quality assurance processes.</p>
          <ul><li>Automated Test Suites</li><li>Performance Testing</li><li>Security Testing</li><li>Mobile Testing</li></ul>
          <div class="more">Learn More</div>
        </article>
        <article class="card service">
          <div class="icon-box"><svg class="ic"><use href="#i-gear"/></svg></div>
          <h3>IT Consulting</h3>
          <p class="desc">Strategic technology consulting to optimize your IT infrastructure and drive digital transformation.</p>
          <ul><li>Digital Strategy</li><li>Technology Assessment</li><li>Process Optimization</li><li>Architecture Design</li></ul>
          <div class="more">Learn More</div>
        </article>
        <article class="card service">
          <div class="icon-box"><svg class="ic"><use href="#i-users"/></svg></div>
          <h3>Team Augmentation</h3>
          <p class="desc">Skilled professionals to extend your development teams with specialized expertise and experience.</p>
          <ul><li>Senior Developers</li><li>QA Specialists</li><li>DevOps Engineers</li><li>Project Managers</li></ul>
          <div class="more">Learn More</div>
        </article>
        <article class="card service">
          <div class="icon-box"><svg class="ic"><use href="#i-db"/></svg></div>
          <h3>Data &amp; Analytics</h3>
          <p class="desc">Transform your data into actionable insights with modern analytics and business intelligence solutions.</p>
          <ul><li>Data Migration</li><li>Analytics Platforms</li><li>Business Intelligence</li><li>Data Governance</li></ul>
          <div class="more">Learn More</div>
        </article>
        <article class="card service">
          <div class="icon-box"><svg class="ic"><use href="#i-cloud"/></svg></div>
          <h3>Cloud Solutions</h3>
          <p class="desc">Comprehensive cloud migration, optimization, and management services for scalable infrastructure.</p>
          <ul><li>Cloud Migration</li><li>DevOps Automation</li><li>Infrastructure as Code</li><li>Monitoring &amp; Alerts</li></ul>
          <div class="more">Learn More</div>
        </article>
        <article class="card service">
          <div class="icon-box"><svg class="ic"><use href="#i-lock"/></svg></div>
          <h3>Cybersecurity</h3>
          <p class="desc">Protect your business with comprehensive security assessments, implementation, and monitoring.</p>
          <ul><li>Security Audits</li><li>Penetration Testing</li><li>Compliance Management</li><li>Incident Response</li></ul>
          <div class="more">Learn More</div>
        </article>
      </div>
    </div>
  </section>

  <section class="expertise">
    <div class="container">
      <div class="head">
        <span class="pill">Technical Excellence</span>
        <h2>Our <span class="accent">Expertise</span></h2>
        <p>Deep technical knowledge across modern technologies and industry best practices, delivering solutions that drive business success and digital transformation.</p>
      </div>
      <div class="exp-grid">
        <article class="card exp">
          <div class="exp-top"><div class="icon-box"><svg class="ic"><use href="#i-search"/></svg></div>
            <div><h3>Testing &amp; Quality Assurance</h3><p class="desc">Comprehensive testing strategies ensuring robust, secure, and high-performance applications</p></div></div>
          <div class="tags"><span>Automated Testing</span><span>Performance Testing</span><span>Security Testing</span><span>API Testing</span><span>Mobile Testing</span><span>Load Testing</span></div>
        </article>
        <article class="card exp">
          <div class="exp-top"><div class="icon-box"><svg class="ic"><use href="#i-building"/></svg></div>
            <div><h3>Development &amp; Architecture</h3><p class="desc">Modern software architecture and development practices for scalable enterprise solutions</p></div></div>
          <div class="tags"><span>Microservices</span><span>Cloud Architecture</span><span>DevOps</span><span>CI/CD</span><span>Infrastructure as Code</span><span>Containerization</span></div>
        </article>
        <article class="card exp">
          <div class="exp-top"><div class="icon-box"><svg class="ic"><use href="#i-cloud"/></svg></div>
            <div><h3>Technologies &amp; Platforms</h3><p class="desc">Cutting-edge cloud platforms and infrastructure technologies for modern applications</p></div></div>
          <div class="tags"><span>Public Cloud</span><span>Private Cloud</span><span>Hybrid Cloud</span><span>Orchestration</span><span>Containers</span><span>IaC Tooling</span><span>CI Servers</span><span>Git Hosting</span></div>
        </article>
        <article class="card exp short">
          <div class="exp-top"><div class="icon-box"><svg class="ic"><use href="#i-gear"/></svg></div>
            <div><h3>Programming &amp; Frameworks</h3><p class="desc">Full-stack development expertise across multiple programming languages and frameworks</p></div></div>
          <div class="tags"><span>JVM</span><span>Scripting</span><span>CLR</span><span>Web UI</span><span>SPA</span><span>JS Runtime</span><span>Microkernels</span><span>Web MVC</span></div>
        </article>
        <article class="card exp short">
          <div class="exp-top"><div class="icon-box"><svg class="ic"><use href="#i-building"/></svg></div>
            <div><h3>Industries</h3><p class="desc">Deep domain knowledge across critical business sectors and regulatory environments</p></div></div>
          <div class="tags"><span>Financial Services</span><span>Healthcare</span><span>E-commerce</span><span>Manufacturing</span><span>Energy</span><span>Telecommunications</span></div>
        </article>
      </div>
      <div class="card cta">
        <div class="icon-box" style="width:38px;height:38px;border-radius:50%"><svg class="ic" style="width:18px;height:18px"><use href="#i-spark"/></svg></div>
        <div><h4>Ready to leverage our expertise?</h4><p>Let's discuss how we can accelerate your digital transformation.</p></div>
      </div>
    </div>
  </section>

  <section class="about">
    <div class="container">
      <div class="about-copy">
        <h2>About <span class="accent">Velmora Systems</span></h2>
        <p>Velmora Systems (formerly BrightHarbor) is a leading IT consulting firm specializing in software testing, quality assurance, and digital transformation for enterprise clients.</p>
        <p>With a global presence spanning Europe and North America, we combine deep technical expertise with industry best practices to deliver innovative solutions that drive business success.</p>
        <p>Our team of seasoned professionals brings decades of experience across various industries, ensuring that every project is executed with precision, quality, and a focus on measurable results.</p>
      </div>
      <div class="stats">
        <div class="card stat"><div class="icon-box"><svg class="ic"><use href="#i-users"/></svg></div><strong>50+</strong><h4>Expert Consultants</h4><p>Seasoned professionals with deep industry expertise</p></div>
        <div class="card stat"><div class="icon-box"><svg class="ic"><use href="#i-globe"/></svg></div><strong>2</strong><h4>Global Markets</h4><p>Serving clients across Europe and North America</p></div>
        <div class="card stat"><div class="icon-box"><svg class="ic"><use href="#i-award"/></svg></div><strong>200+</strong><h4>Projects Delivered</h4><p>Successful implementations across various industries</p></div>
        <div class="card stat"><div class="icon-box"><svg class="ic"><use href="#i-trend"/></svg></div><strong>98%</strong><h4>Client Satisfaction</h4><p>Consistently exceeding client expectations</p></div>
      </div>
    </div>
  </section>

  <section class="contact">
    <div class="container">
      <div class="head">
        <h2>Let's Start Your <span class="accent">Transformation</span></h2>
        <p>Ready to elevate your business with premium IT consulting? Get in touch with our experts today.</p>
      </div>
      <div class="contact-grid">
        <div class="reach">
          <h3>Get in Touch</h3>
          <div class="reach-item"><div class="icon-box"><svg class="ic" style="width:18px;height:18px"><use href="#i-mail"/></svg></div><div><b>Email</b><span>contact@velmora.example</span></div></div>
          <div class="reach-item"><div class="icon-box"><svg class="ic" style="width:18px;height:18px"><use href="#i-phone"/></svg></div><div><b>Phone</b><span>+1 (555) 010-2480</span></div></div>
          <div class="reach-item"><div class="icon-box"><svg class="ic" style="width:18px;height:18px"><use href="#i-pin"/></svg></div><div><b>Locations</b><span>Europe &amp; North America</span></div></div>
          <div class="card why">
            <h4>Why Choose Velmora?</h4>
            <ul><li>Premium quality and enterprise-grade solutions</li><li>Global expertise with local market knowledge</li><li>Proven track record across multiple industries</li><li>Dedicated support throughout your journey</li></ul>
          </div>
        </div>
        <div class="card form">
          <h4>Start Your Project</h4>
          <div class="row">
            <div class="field"><label>First Name</label><div class="input">John</div></div>
            <div class="field"><label>Last Name</label><div class="input">Doe</div></div>
          </div>
          <div class="field"><label>Email</label><div class="input">john.doe@company.com</div></div>
          <div class="field"><label>Company</label><div class="input">Your Company</div></div>
          <div class="field"><label>Project Details</label><div class="input area">Tell us about your project requirements...</div></div>
          <span class="btn btn-primary">Send Message <svg class="ic" style="width:13px;height:13px;stroke:#fff"><use href="#i-send"/></svg></span>
        </div>
      </div>
    </div>
  </section>

  <footer class="footer">
    <div class="container">
      <div class="foot-top">
        <div class="foot-brand"><div class="brand">Velmora Systems</div><p>Premium IT consulting services for enterprise transformation. Delivering innovative solutions in software testing, quality assurance, and digital excellence.</p></div>
        <div class="foot-col"><h5>Services</h5><a>Software Testing</a><a>IT Consulting</a><a>Team Augmentation</a><a>Cloud Solutions</a></div>
        <div class="foot-col"><h5>Company</h5><a>About Us</a><a>Careers</a><a>Contact</a><a>Privacy Policy</a></div>
      </div>
      <div class="foot-bottom"><span>© 2025 Velmora Systems. All rights reserved.</span><span>Formerly BrightHarbor GmbH</span></div>
    </div>
  </footer>
</div>
</body>
</html>
```